Yard sign design for high end luxury home builder.

Need a design for signage on custom homes that are being built. I already have a logo that I am satisfied with that needs to be incorporated. I need the following incorporated in the design of the sign-
- Lic number 318562
- phone number (555) 271-4038
- pendrickhomeworks.com
- Logo/Branding

If possible it may be nice to have the following quote that is on are business cards-

Quote from Osmund of Veltarra-
HE WHO WORKS WITH HIS HANDS IS A LABORER.
HE WHO WORKS WITH HIS HANDS & HIS HEAD IS A CRAFTSMAN.
HE WHO WORKS WITH HIS HANDS & HIS HEAD & HIS HEART IS AN ARTISAN.
-OSMUND OF VELTARRA

Target Market(s)

Archetect, Designers, Clients desiring to build a new home or remodel.

Colors
fde9d4
fee4d5
fabb94
fac994
faa54b
f68d4d
f37122
f78f20
f68e4e

Requirements
Must have
• - Lic number 318562
• - phone number (555) 271-4038
• - pendrickhomeworks.com
• - Logo/Branding
Nice to have
• Quote from Osmund of Veltarra-
• HE WHO WORKS WITH HIS HANDS IS A LABORER.
• HE WHO WORKS WITH HIS HANDS & HIS HEAD IS A CRAFTSMAN.
• HE WHO WORKS WITH HIS HANDS & HIS HEAD & HIS HEART IS AN ARTISAN.
• -OSMUND OF VELTARRA
• OR the below statement-
• Craftsmen that Care
Should not have
• Any additional verbiage not specified above including any type of verbiage about what kind of company we are. For instance- Integrity, reputable... It's just all played out. Im just looking for a bitching design that has the info that compliments my logo/branding.

```html
<!DOCTYPE html>
<html lang="en">
<head>
<meta charset="utf-8">
<title>Pendrick Homeworks – Yard Sign</title>
<link href="https://fonts.googleapis.com/css2?family=Michroma&family=Oswald:wght@700&family=Open+Sans:wght@700;800&display=swap" rel="stylesheet">
<style>
  :root {
    --charcoal: #2b2a29;
    --orange: #f07a2c;
    --orange-deep: #f37122;
    --tan: #b9a48a;
    --white: #ffffff;
    --backdrop: #e9e7e4;
  }
  html, body {
    margin: 0;
    padding: 0;
    width: 1200px;
    height: 1000px;
    overflow: hidden;
    background: var(--backdrop);
  }
  .yard-sign {
    position: absolute;
    left: 250px;
    top: 30px;
    width: 700px;
    height: 940px;
    background: var(--white);
    box-shadow: 0 6px 18px rgba(0,0,0,0.18);
  }
  .sign-face {
    position: absolute;
    left: 20px;
    top: 20px;
    width: 660px;
    height: 900px;
    overflow: hidden;
  }
  .panel-art {
    position: absolute;
    left: 0;
    top: 0;
    width: 660px;
    height: 900px;
  }
  .brand {
    position: absolute;
    left: 0;
    top: 50px;
    width: 660px;
    text-align: center;
    color: var(--tan);
    font-family: "Michroma", sans-serif;
  }
  .brand-square {
    display: block;
    width: 150px;
    height: 150px;
    margin: 0 auto 34px;
    background: var(--tan);
  }
  .brand-name {
    display: block;
    font-size: 46px;
    line-height: 1;
    letter-spacing: 2px;
  }
  .brand-sub {
    display: block;
    margin-top: 12px;
    font-size: 17px;
    letter-spacing: 1.5px;
  }
  .quote {
    position: absolute;
    left: 0;
    top: 560px;
    width: 660px;
    margin: 0;
    text-align: center;
    color: var(--white);
    font-family: "Oswald", sans-serif;
    font-weight: 700;
    font-size: 50px;
    line-height: 62px;
    letter-spacing: -0.5px;
    text-transform: uppercase;
  }
  .license {
    position: absolute;
    left: 0;
    top: 755px;
    width: 660px;
    height: 50px;
    text-align: center;
    font-family: "Open Sans", sans-serif;
    font-weight: 800;
    font-size: 32px;
    line-height: 50px;
  }
  .license-label { color: var(--orange-deep); }
  .license-number { color: var(--charcoal); }
  .contact-bar {
    position: absolute;
    left: 0;
    top: 808px;
    width: 660px;
    height: 92px;
    display: flex;
    align-items: center;
    justify-content: center;
    gap: 18px;
    color: var(--white);
    font-family: "Open Sans", sans-serif;
    font-weight: 700;
  }
  .contact-phone {
    display: flex;
    align-items: center;
    gap: 12px;
    font-size: 36px;
  }
  .contact-divider {
    width: 2px;
    height: 42px;
    background: var(--white);
  }
  .contact-web {
    display: flex;
    align-items: center;
    gap: 8px;
    font-size: 19px;
  }
</style>
</head>
<body>
  <div class="yard-sign">
    <div class="sign-face">
      <svg class="panel-art" viewBox="0 0 660 900" aria-hidden="true">
        <rect x="0" y="0" width="660" height="755" fill="var(--orange)"/>
        <polygon points="0,0 660,0 660,375 330,525 0,375" fill="var(--charcoal)"/>
        <rect x="0" y="755" width="660" height="50" fill="var(--white)"/>
        <rect x="0" y="805" width="660" height="3" fill="var(--orange-deep)"/>
        <rect x="0" y="808" width="660" height="92" fill="var(--charcoal)"/>
      </svg>

      <div class="brand">
        <span class="brand-square"></span>
        <span class="brand-name">PENDRICK</span>
        <span class="brand-sub">HOMEWORKS INC.</span>
      </div>

      <p class="quote">He who works<br>with his hands &amp; his head<br>is a craftsman</p>

      <div class="license">
        <span class="license-label">LIC NUMBER</span>
        <span class="license-number">318562</span>
      </div>

      <div class="contact-bar">
        <span class="contact-phone">
          <svg width="34" height="34" viewBox="0 0 24 24" aria-hidden="true">
            <path fill="var(--orange)" d="M6.6 10.8a15.1 15.1 0 0 0 6.6 6.6l2.2-2.2a1 1 0 0 1 1-.25 11.4 11.4 0 0 0 3.6.57 1 1 0 0 1 1 1V20a1 1 0 0 1-1 1A17 17 0 0 1 3 4a1 1 0 0 1 1-1h3.5a1 1 0 0 1 1 1c0 1.25.2 2.45.57 3.57a1 1 0 0 1-.25 1z"/>
            <path fill="none" stroke="var(--orange)" stroke-width="1.8" stroke-linecap="round" d="M14.5 3.5a6 6 0 0 1 6 6M14.5 7a2.6 2.6 0 0 1 2.6 2.6"/>
          </svg>
          (555) 271-4038
        </span>
        <span class="contact-divider"></span>
        <span class="contact-web">
          <svg width="22" height="22" viewBox="0 0 24 24" aria-hidden="true">
            <g fill="none" stroke="var(--orange)" stroke-width="1.8">
              <circle cx="12" cy="12" r="10"/>
              <ellipse cx="12" cy="12" rx="4.5" ry="10"/>
              <path d="M2 12h20M4 6.5h16M4 17.5h16"/>
            </g>
          </svg>
          pendrickhomeworks.com
        </span>
      </div>
    </div>
  </div>
</body>
</html>
```